Business card for Eyelash extension salon in Ashford Glen,California USA

We need new business card for our salon in Ashford Glen. The salon name is 'Lumarra' . We would like to have...Business name: Lumarra Name of person: will provide later Address 6128 N.Corbel Ridge Blvd Ashford Glen , CA 90210 Phone: will provide later (Text only) Web: www.lumarrastudio-example.com Pictogrid icon, Friendvale icon follow us for seasonal campaign and news @lumarrastudioexample Design should look elegant, high-end, clean, simple, cohesive with my brand. Please refer my brand board. Business name color will be metallic bronzy color. Im thinking grey background or white background. Thanks

Target Market(s)

25-35. Gender neutral. People who are in Entertainment business industry.
This is High-end Eyelash extension salon in Ashford Glen

Industry/Entity Type

Beauty Salon

Contact Information for Business Card

Business name: Lumarra
Name of person: will provide later
Address 6128 N.Corbel Ridge Blvd Ashford Glen , CA 90210
Phone: will provide later (Text only)
Web: www.lumarrastudio-example.com
Pictogrid icon, Friendvale icon
follow us for seasonal campaign and news @lumarrastudioexample

Requirements
Must have
• Beautiful, elegant, clean and simple look but very attractive and modern
Should not have
• We don't like too clutter, too busy designs.

```html
<!DOCTYPE html>
<html lang="en">
<head>
<meta charset="utf-8">
<title>Lumarra Ashford Glen – Business Card</title>
<link rel="stylesheet" href="https://fonts.googleapis.com/css2?family=Playfair+Display:wght@400;700&family=Josefin+Sans:wght@400&display=swap">
<style>
  :root {
    --bronze: #8a6a50;
    --stone-grey: #a8a8a8;
    --text-grey: #a3a3a3;
    --marble-light: #f1f1f1;
    --marble-mid: #d9d9d9;
    --paper: #ffffff;
  }
  * { margin: 0; padding: 0; box-sizing: border-box; }
  html, body {
    width: 1200px; height: 1000px; overflow: hidden;
    background: var(--paper);
  }
  .canvas { position: relative; width: 1200px; height: 1000px; }

  .card { position: absolute; left: 53px; width: 659px; height: 365px; }

  /* Front */
  .card-front { top: 92px; }
  .card-front .backdrop { position: absolute; inset: 0; width: 100%; height: 100%; }
  .logo-panel {
    position: absolute; left: 137px; top: 52px; width: 385px; height: 262px;
    background: var(--paper); border: 8px solid var(--bronze);
  }
  .brand-name {
    position: absolute; left: 0; right: 0; top: 52px; text-align: center;
    font-family: "Playfair Display", serif; font-weight: 400;
    font-size: 78px; line-height: 1.2; color: var(--bronze); letter-spacing: 1px;
  }
  .brand-location {
    position: absolute; right: 67px; top: 197px;
    font-family: "Josefin Sans", sans-serif; font-size: 11px;
    letter-spacing: 2px; color: var(--bronze);
  }

  /* Back */
  .card-back {
    top: 544px; height: 366px;
    border: 13px solid var(--bronze); background: var(--paper);
    font-family: "Playfair Display", serif; color: var(--text-grey);
    font-variant-numeric: lining-nums;
  }
  .person-name {
    position: absolute; left: 0; right: 0; top: 40px; text-align: center;
    font-weight: 700; font-size: 64px; line-height: 1;
  }
  .divider {
    position: absolute; left: 40px; right: 40px; top: 127px; height: 7px;
    background: var(--bronze);
  }
  .contact-line {
    position: absolute; left: 40px; right: 40px;
    font-size: 23px; line-height: 1; display: flex; justify-content: space-between;
  }
  .contact-address { top: 165px; }
  .contact-phone-web { top: 197px; }
  .follow-note {
    position: absolute; left: 0; right: 0; top: 246px; text-align: center;
    font-size: 18px;
  }
  .social-row {
    position: absolute; left: 0; right: 0; top: 277px;
    display: flex; justify-content: center; align-items: center; gap: 9px;
    font-size: 18px;
  }
  .social-dot {
    width: 22px; height: 22px; border-radius: 50%; background: var(--text-grey);
  }
  .social-handle { margin-left: 3px; }
</style>
</head>
<body>
<main class="canvas">

  <section class="card card-front" aria-label="Business card front">
    <svg class="backdrop" viewBox="0 0 659 365" preserveAspectRatio="none" aria-hidden="true">
      <defs>
        <linearGradient id="marbleTone" x1="0" y1="0" x2="1" y2="1">
          <stop offset="0" stop-color="#f1f1f1"/>
          <stop offset="0.5" stop-color="#d9d9d9"/>
          <stop offset="1" stop-color="#f1f1f1"/>
        </linearGradient>
      </defs>
      <rect width="659" height="365" fill="#a8a8a8"/>
      <polygon points="0,0 659,0 0,365" fill="url(#marbleTone)" role="img" aria-label="White marble texture"/>
    </svg>
    <div class="logo-panel">
      <div class="brand-name">Lumarra</div>
      <div class="brand-location">ASHFORD GLEN</div>
    </div>
  </section>

  <section class="card card-back" aria-label="Business card back">
    <h1 class="person-name">John Doe</h1>
    <div class="divider"></div>
    <p class="contact-line contact-address"><span>6128 N. Corbel Ridge Blvd. Ashford Glen CA 90477</span></p>
    <p class="contact-line contact-phone-web"><span>000 000 0000</span><span>www.lumarrastudio-example.com</span></p>
    <p class="follow-note">Follow us for seasonal campaign and news:</p>
    <div class="social-row">
      <span class="social-dot" role="img" aria-label="Friendvale"></span>
      <span class="social-dot" role="img" aria-label="Pictogrid"></span>
      <span class="social-handle">@lumarrastudioexample</span>
    </div>
  </section>

</main>
</body>
</html>
```